AUSTRALIA SUPPLEMENT - Protein label design - CREATIVE, FEMININE, UNIQUE

I need help with the design of what will be my line of supplements. (Protein, plant base, collagen , BCAAs, etc)
I'm starting off with protein isolate - with the flavours VANILLA, CHOCOLATE, BOYSENBERRY, HONEYCOMB.
I need help with the design of what the product will look like for my range.
(Great opportunity for further work)

Looking for a unique, elegant, stand out, feminine design, some slight sparkle or something that stands out on a shelf.
With symbols to represent what's in it, raised text. with some quirky cute things on it. (not sure what) Something that captured young womens eyes and easy to understand. things on it that appeals to women such as
LOW CALORIE, GREAT TASTING, GLUTEN FREE, 100 NATURAL, NATURALLY SWEETENED, HIGH PROTEIN.etc and whatever you can think of (open to ideas) but within KMO guidelines.

Mostly just after the look and creativity of what the front will look like. Don't have to worry about the back area.

My market will be for females aged 18-35

I have a activewear line called DORUMEN which will go with this. which I will attach the logo below amongst some other things that match my packaging. (again open to ideas)

I have attached a label of what one will look like( EXAMPLE).
. Among others that look nice But again I want to be different, unique to stand out. I don't want it to look like these. it's just the only ones I found online I liked that suit my market.

Feel free to ask any questions! :)
Updates

Extending time as I want this to be to be what will be on the shelves of many stores. I know that needs time to be able to do a quality job.

Target Market(s)

18-35

Industry/Entity Type

Supplement

Font styles to use
Serif
Script

Colors
f9d9e8
ffffff
fbd3d4
ecf7fb
e4daeb
cfeae6
eea4c8
fdfad7
f59195

Requirements
Must have
• Word - DORUMEN
PROTEIN ISOLATE
FLAVOUR
SYMBOLS

Looking for a unique, elegant, stand out, colour, feminine design, some slight sparkle or something that stands out on a shelf.

IT WILL BE ON A WHITE TUB or CLEAR - Perhaps detail on the lid
Nice to have
• Looking for a unique, elegant, stand out, colour, feminine design, some slight sparkle or something that stands out on a shelf. Something artsy.

will be on a white or clear tub with a white label background (possibly)
Should not have
• I don’t want it dark looking.
Something bright, vibrant, whites, pinks, sparkles (maybe) colours.

I don't want the word activewear on it.

```html
<!DOCTYPE html>
<html lang="en">
<head>
<meta charset="utf-8">
<title>DORUMEN Protein Isolate – Boysenberry Label</title>
<link href="https://fonts.googleapis.com/css2?family=Barlow:wght@400;500;600&family=Cormorant+Garamond:wght@500&family=Poiret+One&display=swap" rel="stylesheet">
<style>
  :root {
    --stage: #ececee;
    --label-white: #ffffff;
    --blush: #f9d9e8;
    --petal: #fbd3d4;
    --lilac: #e4daeb;
    --sage: #cfd6d2;
    --rose-text: #c9738f;
    --panel-pink: rgba(226, 134, 168, 0.86);
    --frame-line: rgba(255, 255, 255, 0.85);
    --ink-light: #ffffff;
  }
  * { margin: 0; padding: 0; box-sizing: border-box; }
  html, body { width: 1200px; height: 1000px; overflow: hidden; }
  body {
    background: linear-gradient(180deg, #f4f4f4 0%, #e6e6e8 60%, #d4d3d7 100%);
    position: relative;
  }
  .label {
    position: absolute;
    left: 250px; top: 40px;
    width: 700px; height: 920px;
    background: var(--label-white);
    overflow: hidden;
    box-shadow: 0 6px 24px rgba(0,0,0,0.08);
  }
  .floral-pattern {
    position: absolute; inset: 0;
    background:
      radial-gradient(circle at 10% 14%, var(--blush) 0 70px, transparent 120px),
      radial-gradient(circle at 92% 10%, var(--lilac) 0 55px, transparent 110px),
      radial-gradient(circle at 88% 24%, var(--blush) 0 70px, transparent 120px),
      radial-gradient(circle at 6% 50%, var(--petal) 0 50px, transparent 100px),
      radial-gradient(circle at 62% 36%, var(--petal) 0 60px, transparent 120px),
      radial-gradient(circle at 95% 62%, var(--blush) 0 60px, transparent 110px),
      radial-gradient(circle at 8% 78%, var(--lilac) 0 50px, transparent 100px),
      radial-gradient(circle at 30% 96%, var(--petal) 0 60px, transparent 110px),
      radial-gradient(circle at 85% 94%, var(--lilac) 0 50px, transparent 100px),
      radial-gradient(circle at 30% 30%, var(--sage) 0 20px, transparent 60px),
      radial-gradient(circle at 78% 50%, var(--sage) 0 18px, transparent 55px),
      var(--label-white);
    opacity: 0.9;
  }
  .brand-name {
    position: absolute;
    left: 0; right: 0; top: 270px;
    text-align: center;
    font-family: "Cormorant Garamond", serif;
    font-weight: 500;
    font-size: 64px;
    letter-spacing: 0.28em;
    padding-left: 0.28em;
    color: var(--rose-text);
  }
  .product-panel {
    position: absolute;
    left: 143px; top: 430px;
    width: 414px; height: 414px;
    background: var(--panel-pink);
    color: var(--ink-light);
    text-align: center;
  }
  .panel-frame {
    position: absolute; inset: 12px;
    border: 2px solid var(--frame-line);
  }
  .product-type {
    position: absolute; left: 0; right: 0; top: 42px;
    font-family: "Poiret One", sans-serif;
    font-size: 62px;
    line-height: 54px;
    letter-spacing: 0.02em;
  }
  .divider {
    position: absolute; left: 105px; width: 204px; top: 194px;
    height: 2px; background: var(--ink-light);
  }
  .flavour {
    position: absolute; left: 0; right: 0; top: 220px;
    font-family: "Barlow", sans-serif;
    font-weight: 500;
    font-size: 33px;
    letter-spacing: 0.12em;
  }
  .claim {
    position: absolute; left: 0; right: 0; top: 272px;
    font-family: "Barlow", sans-serif;
    font-weight: 600;
    font-size: 15px;
  }
  .benefits {
    position: absolute; left: 60px; right: 60px; top: 302px;
    display: flex; justify-content: space-between;
    list-style: none;
  }
  .benefit {
    width: 90px;
    display: flex; flex-direction: column; align-items: center;
    font-family: "Barlow", sans-serif;
    font-size: 12px; line-height: 12px;
    letter-spacing: 0.06em;
  }
  .benefit svg { width: 42px; height: 42px; margin-bottom: 6px; }
</style>
</head>
<body>
  <main class="label">
    <div class="floral-pattern" role="img" aria-label="Soft watercolour pattern of pale pink and lilac blossoms with grey-green leaves"></div>

    <h1 class="brand-name">DORUMEN</h1>

    <section class="product-panel">
      <div class="panel-frame"></div>
      <h2 class="product-type">PROTEIN<br>ISOLATE</h2>
      <div class="divider"></div>
      <p class="flavour">BOYSENBERRY</p>
      <p class="claim">HIGH PROTEIN - NATURALLY SWEETENED</p>
      <ul class="benefits">
        <li class="benefit">
          <svg viewBox="0 0 42 42" fill="none" stroke="#fff" stroke-width="1.6" stroke-linecap="round">
            <circle cx="21" cy="21" r="19"/>
            <path d="M21 21 L12 11"/>
            <path d="M21 6v3M8 21h3M31 21h3M11 11l2 2M31 11l-2 2"/>
            <circle cx="21" cy="21" r="2" fill="#fff"/>
          </svg>
          LOW<br>CALORIE
        </li>
        <li class="benefit">
          <svg viewBox="0 0 42 42" fill="none" stroke="#fff" stroke-width="1.6" stroke-linecap="round">
            <circle cx="21" cy="21" r="19"/>
            <path d="M21 33V12"/>
            <path d="M21 16c-4-1-5-4-5-6M21 16c4-1 5-4 5-6M21 22c-4-1-5-4-5-6M21 22c4-1 5-4 5-6M21 28c-4-1-5-4-5-6M21 28c4-1 5-4 5-6"/>
          </svg>
          GLUTEN<br>FREE
        </li>
        <li class="benefit">
          <svg viewBox="0 0 42 42" fill="#fff">
            <path d="M12 24C6 18 8 8 14 4c4 6 6 14-2 20z"/>
            <path d="M18 34c0-10 8-16 18-14-2 10-10 16-18 14z"/>
            <path d="M12 24 L18 34" stroke="#fff" stroke-width="1.6"/>
          </svg>
          100%<br>NATURAL
        </li>
      </ul>
    </section>
  </main>
</body>
</html>
```